Design a PSD Brochure Template

We need a PSD design template for a product catalogue.

Needs to be A4 horizontal/landscape.

Please design a page similar layout to the attached and include on page:
- front page Design
- our logo
- basic footer with email address, phone number and website
- Basic border/design

There will be 5-6 different pages that need to be designed once freelancer is awarded

```html
<!DOCTYPE html>
<html lang="en">
<head>
<meta charset="utf-8">
<title>Product List – French Bistro Chair &amp; Alu. Table Base</title>
<link rel="stylesheet" href="https://fonts.googleapis.com/css2?family=Montserrat:ital,wght@0,500;0,700;1,800&family=Questrial&display=swap">
<style>
  :root{
    --navy:#163a6b;
    --navy-deep:#0f2f5c;
    --blue-line:#2c5f9e;
    --orange:#f39a1e;
    --paper:#ffffff;
    --backdrop:#cdc7c4;
    --ink:#2a3a52;
    --muted:#6b7686;
    --rattan-a:#d9c29a;
    --rattan-b:#9a7a52;
    --alu-a:#eef1f4;
    --alu-b:#a9b2bd;
  }
  *{box-sizing:border-box;margin:0;padding:0}
  html,body{width:1200px;height:832px;overflow:hidden}
  body{background:var(--backdrop);font-family:"Montserrat",sans-serif;color:var(--ink);position:relative}

  /* A4 landscape sheet (297 × 210 ratio), folded into two panels */
  .sheet{position:absolute;left:40px;top:20px;width:1120px;height:792px;display:flex;box-shadow:0 6px 24px rgba(0,0,0,.18)}
  .page{position:relative;width:560px;height:792px;background:var(--paper);overflow:hidden}
  .page--left{border-right:1px solid #e1e4e8}

  .frame{position:absolute;left:18px;top:18px;right:18px;bottom:42px;border:1.5px solid var(--navy);border-radius:14px}

  .tab{position:absolute;left:18px;top:18px;height:38px;width:190px;background:var(--navy);
       clip-path:polygon(0 0,100% 0,86% 100%,0 100%);border-top-left-radius:14px;
       display:flex;align-items:center;padding-left:20px;
       font-weight:800;font-style:italic;font-size:14px;letter-spacing:.5px;color:#fff;white-space:nowrap}
  .page--right .tab{color:var(--orange)}
  .title{position:absolute;right:40px;top:30px;font-family:"Questrial",sans-serif;font-weight:400;font-size:21px;line-height:26px;color:var(--ink);white-space:nowrap}
  .title-rule{position:absolute;left:200px;right:30px;top:62px;height:3px;background:var(--navy);border-radius:2px}

  .brand{position:absolute;right:28px;top:72px;display:flex;align-items:center;gap:5px;
         font-weight:700;font-size:8px;line-height:10px;color:var(--navy);white-space:nowrap}
  .brand i{width:10px;height:10px;border-radius:50%;background:var(--navy)}

  .grid{position:absolute;display:grid;justify-items:center;align-items:center}
  .grid--chairs{left:30px;right:30px;top:82px;height:650px;grid-template-columns:repeat(4,1fr);grid-template-rows:repeat(5,1fr)}
  .grid--top{left:30px;right:30px;top:92px;height:230px;grid-template-columns:repeat(5,1fr);grid-template-rows:repeat(2,1fr)}
  .panel{position:absolute;left:26px;right:26px;top:332px;height:400px;background:linear-gradient(160deg,#1d4a80,var(--navy-deep));border-radius:16px}
  .grid--panel{left:36px;right:36px;top:342px;height:380px;grid-template-columns:repeat(5,1fr);grid-template-rows:repeat(3,1fr)}

  .item{display:flex;flex-direction:column;align-items:center;gap:3px}
  .ph{width:44px;height:50px;border-radius:6px}
  .ph--chair{background:linear-gradient(170deg,var(--rattan-a),var(--rattan-b))}
  .ph--base{width:40px;height:42px;background:linear-gradient(170deg,var(--alu-a),var(--alu-b))}
  .grid--panel .ph--base{height:52px;background:linear-gradient(170deg,#dfe5ec,#7f8b99)}
  .tag{display:block;width:86px;height:10px;border-radius:5px;background:var(--navy);color:#fff;
       font-size:6px;font-weight:700;line-height:10px;text-align:center;letter-spacing:.4px;white-space:nowrap}
  .grid--panel .tag{background:#fff;color:var(--navy)}
  .meta{display:flex;align-items:center;gap:2px;line-height:10px}
  .meta i{width:6px;height:6px;border-radius:50%;background:#8a8f96}
  .meta i:nth-child(2){background:#5b4a3a}
  .meta i:nth-child(3){background:#c9b08a}
  .meta b{margin-left:5px;font-size:8px;font-weight:500;color:var(--ink);white-space:nowrap}
  .grid--panel .meta b{color:#fff}
  .grid--panel .meta i:nth-child(3){background:#e7e9ec}

  .footer{position:absolute;left:0;right:0;bottom:0;height:32px;border-top:3px solid var(--blue-line);
          display:flex;align-items:center;padding:0 28px;font-size:6.5px;line-height:10px;color:var(--muted);letter-spacing:.3px;white-space:nowrap}
  .page--right .footer{justify-content:flex-end}
</style>
</head>
<body>
<main class="sheet">

  <section class="page page--left">
    <div class="frame"></div>
    <div class="tab">PRODUCT LIST</div>
    <h2 class="title">French Bistro Chair</h2>
    <div class="title-rule"></div>

    <div class="grid grid--chairs">
      <div class="item"><div class="ph ph--chair" role="img" aria-label="Rattan bistro chair"></div><span class="tag">BC-101</span><div class="meta"><i></i><i></i><i></i><b>$ 248</b></div></div>
      <div class="item"><div class="ph ph--chair" role="img" aria-label="Rattan bistro armchair"></div><span class="tag">BC-102</span><div class="meta"><i></i><i></i><i></i><b>$ 248</b></div></div>
      <div class="item"><div class="ph ph--chair" role="img" aria-label="Rattan bistro armchair"></div><span class="tag">BC-103</span><div class="meta"><i></i><i></i><i></i><b>$ 248</b></div></div>
      <div class="item"><div class="ph ph--chair" role="img" aria-label="Rattan bistro chair"></div><span class="tag">BC-104</span><div class="meta"><i></i><i></i><i></i><b>$ 248</b></div></div>
      <div class="item"><div class="ph ph--chair" role="img" aria-label="Green woven bistro chair"></div><span class="tag">BC-105</span><div class="meta"><i></i><i></i><i></i><b>$ 248</b></div></div>
      <div class="item"><div class="ph ph--chair" role="img" aria-label="Woven bistro armchair"></div><span class="tag">BC-106</span><div class="meta"><i></i><i></i><i></i><b>$ 248</b></div></div>
      <div class="item"><div class="ph ph--chair" role="img" aria-label="Red woven bistro chair"></div><span class="tag">BC-107</span><div class="meta"><i></i><i></i><i></i><b>$ 248</b></div></div>
      <div class="item"><div class="ph ph--chair" role="img" aria-label="Woven bistro chair"></div><span class="tag">BC-108</span><div class="meta"><i></i><i></i><i></i><b>$ 248</b></div></div>
      <div class="item"><div class="ph ph--chair" role="img" aria-label="Rattan bistro armchair"></div><span class="tag">BC-109</span><div class="meta"><i></i><i></i><i></i><b>$ 248</b></div></div>
      <div class="item"><div class="ph ph--chair" role="img" aria-label="Rattan bistro chair"></div><span class="tag">BC-110</span><div class="meta"><i></i><i></i><i></i><b>$ 248</b></div></div>
      <div class="item"><div class="ph ph--chair" role="img" aria-label="Rattan bistro chair"></div><span class="tag">BC-111</span><div class="meta"><i></i><i></i><i></i><b>$ 248</b></div></div>
      <div class="item"><div class="ph ph--chair" role="img" aria-label="Woven bistro chair"></div><span class="tag">BC-112</span><div class="meta"><i></i><i></i><i></i><b>$ 248</b></div></div>
      <div class="item"><div class="ph ph--chair" role="img" aria-label="Dark rattan armchair"></div><span class="tag">BC-113</span><div class="meta"><i></i><i></i><i></i><b>$ 248</b></div></div>
      <div class="item"><div class="ph ph--chair" role="img" aria-label="Dark rattan armchair"></div><span class="tag">BC-114</span><div class="meta"><i></i><i></i><i></i><b>$ 248</b></div></div>
      <div class="item"><div class="ph ph--chair" role="img" aria-label="Rattan bistro armchair"></div><span class="tag">BC-115</span><div class="meta"><i></i><i></i><i></i><b>$ 248</b></div></div>
      <div class="item"><div class="ph ph--chair" role="img" aria-label="Woven bistro chair"></div><span class="tag">BC-116</span><div class="meta"><i></i><i></i><i></i><b>$ 248</b></div></div>
      <div class="item"><div class="ph ph--chair" role="img" aria-label="Grey woven chair"></div><span class="tag">BC-117</span><div class="meta"><i></i><i></i><i></i><b>$ 248</b></div></div>
      <div class="item"><div class="ph ph--chair" role="img" aria-label="Dark woven armchair"></div><span class="tag">BC-118</span><div class="meta"><i></i><i></i><i></i><b>$ 248</b></div></div>
      <div class="item"><div class="ph ph--chair" role="img" aria-label="Grey woven chair"></div><span class="tag">BC-119</span><div class="meta"><i></i><i></i><i></i><b>$ 248</b></div></div>
      <div class="item"><div class="ph ph--chair" role="img" aria-label="Metal frame bistro chair"></div><span class="tag">BC-120</span><div class="meta"><i></i><i></i><i></i><b>$ 248</b></div></div>
    </div>

    <footer class="footer">Tel 555 0142 · info@fernwoodsupply.com · www.fernwoodsupply.com</footer>
  </section>

  <section class="page page--right">
    <div class="frame"></div>
    <div class="tab">PRODUCT LIST</div>
    <h2 class="title">Alu. Table Base</h2>
    <div class="title-rule"></div>
    <div class="brand"><i></i>FERNWOOD SUPPLY</div>

    <div class="grid grid--top">
      <div class="item"><div class="ph ph--base" role="img" aria-label="Aluminium cross table base"></div><span class="tag">TB-201</span><div class="meta"><i></i><i></i><i></i><b>$ 248</b></div></div>
      <div class="item"><div class="ph ph--base" role="img" aria-label="Aluminium cross table base"></div><span class="tag">TB-202</span><div class="meta"><i></i><i></i><i></i><b>$ 248</b></div></div>
      <div class="item"><div class="ph ph--base" role="img" aria-label="Aluminium table base"></div><span class="tag">TB-203</span><div class="meta"><i></i><i></i><i></i><b>$ 248</b></div></div>
      <div class="item"><div class="ph ph--base" role="img" aria-label="Aluminium table base"></div><span class="tag">TB-204</span><div class="meta"><i></i><i></i><i></i><b>$ 248</b></div></div>
      <div class="item"><div class="ph ph--base" role="img" aria-label="Bronze table base"></div><span class="tag">TB-205</span><div class="meta"><i></i><i></i><i></i><b>$ 248</b></div></div>
      <div class="item"><div class="ph ph--base" role="img" aria-label="Red four leg table base"></div><span class="tag">TB-206</span><div class="meta"><i></i><i></i><i></i><b>$ 248</b></div></div>
      <div class="item"><div class="ph ph--base" role="img" aria-label="Aluminium four leg base"></div><span class="tag">TB-207</span><div class="meta"><i></i><i></i><i></i><b>$ 248</b></div></div>
      <div class="item"><div class="ph ph--base" role="img" aria-label="Aluminium table base"></div><span class="tag">TB-208</span><div class="meta"><i></i><i></i><i></i><b>$ 248</b></div></div>
      <div class="item"><div class="ph ph--base" role="img" aria-label="Aluminium table base"></div><span class="tag">TB-209</span><div class="meta"><i></i><i></i><i></i><b>$ 248</b></div></div>
      <div class="item"><div class="ph ph--base" role="img" aria-label="Aluminium table base"></div><span class="tag">TB-210</span><div class="meta"><i></i><i></i><i></i><b>$ 248</b></div></div>
    </div>

    <div class="panel"></div>
    <div class="grid grid--panel">
      <div class="item"><div class="ph ph--base" role="img" aria-label="Cast twin table base"></div><span class="tag">TB-301</span><div class="meta"><i></i><i></i><i></i><b>$ 248</b></div></div>
      <div class="item"><div class="ph ph--base" role="img" aria-label="Cast table base"></div><span class="tag">TB-302</span><div class="meta"><i></i><i></i><i></i><b>$ 248</b></div></div>
      <div class="item"><div class="ph ph--base" role="img" aria-label="Cast table base"></div><span class="tag">TB-303</span><div class="meta"><i></i><i></i><i></i><b>$ 248</b></div></div>
      <div class="item"><div class="ph ph--base" role="img" aria-label="Cast table base"></div><span class="tag">TB-304</span><div class="meta"><i></i><i></i><i></i><b>$ 248</b></div></div>
      <div class="item"><div class="ph ph--base" role="img" aria-label="Cast twin table base"></div><span class="tag">TB-305</span><div class="meta"><i></i><i></i><i></i><b>$ 248</b></div></div>
      <div class="item"><div class="ph ph--base" role="img" aria-label="Cast cross table base"></div><span class="tag">TB-306</span><div class="meta"><i></i><i></i><i></i><b>$ 248</b></div></div>
      <div class="item"><div class="ph ph--base" role="img" aria-label="Cast table base"></div><span class="tag">TB-307</span><div class="meta"><i></i><i></i><i></i><b>$ 248</b></div></div>
      <div class="item"><div class="ph ph--base" role="img" aria-label="Cast cross table base"></div><span class="tag">TB-308</span><div class="meta"><i></i><i></i><i></i><b>$ 248</b></div></div>
      <div class="item"><div class="ph ph--base" role="img" aria-label="Cast table base"></div><span class="tag">TB-309</span><div class="meta"><i></i><i></i><i></i><b>$ 248</b></div></div>
      <div class="item"><div class="ph ph--base" role="img" aria-label="Cast twin table base"></div><span class="tag">TB-310</span><div class="meta"><i></i><i></i><i></i><b>$ 248</b></div></div>
      <div class="item"><div class="ph ph--base" role="img" aria-label="Round disc table base"></div><span class="tag">TB-311</span><div class="meta"><i></i><i></i><i></i><b>$ 248</b></div></div>
      <div class="item"><div class="ph ph--base" role="img" aria-label="Round disc table base"></div><span class="tag">TB-312</span><div class="meta"><i></i><i></i><i></i><b>$ 248</b></div></div>
      <div class="item"><div class="ph ph--base" role="img" aria-label="Round disc table base"></div><span class="tag">TB-313</span><div class="meta"><i></i><i></i><i></i><b>$ 248</b></div></div>
      <div class="item"><div class="ph ph--base" role="img" aria-label="Oval disc table base"></div><span class="tag">TB-314</span><div class="meta"><i></i><i></i><i></i><b>$ 248</b></div></div>
      <div class="item"><div class="ph ph--base" role="img" aria-label="Cast twin table base"></div><span class="tag">TB-315</span><div class="meta"><i></i><i></i><i></i><b>$ 248</b></div></div>
    </div>

    <footer class="footer">Tel 555 0142 · info@fernwoodsupply.com · www.fernwoodsupply.com</footer>
  </section>

</main>
</body>
</html>
```